Digital Billboard Design: Winter Sales Event

I own a boutique furniture store in Calgary, AB (maplewoven.ca) and I am looking to advertise our winter sale event on a new curved digital billboard (specs attached including required file type).

I have this billboard rented for 52-weeks so I will be looking to change the design every 4-weeks (i.e. this is intended to be an ongoing project).

The objective of this first billboard is to raise awareness around our annual winter sales event. The store itself is only a few blocks from the billboard so those commuting into downtown are just a short drive from the store.

I am looking for a fresh, clean, contemporary look that will grab your attention as you drive into downtown Calgary without presenting to much info so as to be distracting (and overwhelming -- the billboard does not need to contain all info on my current marketing material). I should also note that the store caters to a higher-end, more sophisticated clientele so the graphics need to reflect the brand (i.e. we are not Brenton Furniture or Couch Depot!).

I have attached three files:

Billboard specs
Current marketing material advertising sale (and all relevant data)
An idea that is from an American furniture store that I think is interesting

Target Market(s)

Upper middle class, sophisticated client who appreciates the finer things in life.

Industry/Entity Type

Furniture Store

Font styles to use
Sans Serif

Requirements
Must have
• Company Logo
• Winter Sales Event - 20 to 60% off
• Address: 3847 22nd Ave SW
Nice to have
• Image of furniture -- see our website www.maplewoven.ca -- any photo from this site can be used
Should not have
• Too much text or visual distration

```html
<!DOCTYPE html>
<html lang="en">
<head>
<meta charset="utf-8">
<title>Maple Woven – Winter Sales Event</title>
<link rel="stylesheet" href="https://fonts.googleapis.com/css2?family=Open+Sans:wght@300;400;600;700&display=swap">
<style>
  :root {
    --slate: #5d6670;
    --paper: #ffffff;
    --page: #ffffff;
    --bed-dark: #3c3e42;
    --bed-light: #6a6d72;
    --oak-dark: #cdb394;
    --oak-light: #e6d3bc;
    --shade: #1b1b28;
    --coral: #d9321f;
    --walnut-dark: #5c4530;
    --walnut-light: #7d6246;
    --ebony: #1c1c1c;
    --ebony-light: #3a3a3a;
  }
  * { margin: 0; padding: 0; box-sizing: border-box; }
  html, body {
    width: 1200px; height: 767px; overflow: hidden;
    background: var(--page);
    font-family: "Open Sans", sans-serif;
  }
  .billboard {
    position: absolute; left: 85px; top: 75px;
    width: 1025px; height: 585px;
    background: var(--paper);
    box-shadow: 0 4px 18px rgba(0,0,0,0.35);
  }
  .masthead {
    position: absolute; left: 0; top: 0; width: 100%; height: 143px;
    background: var(--slate);
  }
  .brand-name {
    position: absolute; left: 0; top: 46px; width: 100%;
    text-align: center; color: var(--paper);
    font-size: 54px; font-weight: 600; letter-spacing: 6px; line-height: 1;
  }
  .rule { position: absolute; height: 3px; background: var(--paper); }
  .rule--top { left: 187px; top: 127px; width: 649px; }
  .rule--bottom { left: 183px; top: 458px; width: 650px; }
  .headline {
    position: absolute; left: 0; top: 150px; width: 100%;
    text-align: center; color: var(--slate);
    font-size: 34px; font-weight: 700; line-height: 1; white-space: nowrap;
  }
  .headline .dash { font-weight: 400; }
  .headline .big { font-size: 44px; font-weight: 600; }
  .headline .light { font-weight: 400; font-size: 26px; }
  .headline .off { font-weight: 400; }
  .product { position: absolute; border-radius: 4px; }
  .product--bed {
    left: 35px; top: 258px; width: 168px; height: 124px;
    background: linear-gradient(180deg, var(--bed-light) 0%, var(--bed-dark) 100%);
  }
  .product--table {
    left: 213px; top: 265px; width: 184px; height: 124px;
    background: linear-gradient(180deg, var(--oak-light) 0%, var(--oak-dark) 100%);
  }
  .product--lamp {
    left: 427px; top: 223px; width: 58px; height: 183px;
    background: linear-gradient(180deg, var(--shade) 0%, var(--shade) 35%, var(--coral) 65%, var(--coral) 100%);
  }
  .product--dresser {
    left: 558px; top: 247px; width: 244px; height: 128px;
    background: linear-gradient(180deg, var(--walnut-light) 0%, var(--walnut-dark) 100%);
  }
  .product--side-table {
    left: 861px; top: 262px; width: 137px; height: 126px;
    background: linear-gradient(180deg, var(--ebony-light) 0%, var(--ebony) 100%);
  }
  .footer {
    position: absolute; left: 0; top: 443px; width: 100%; height: 142px;
    background: var(--slate);
  }
  .address {
    position: absolute; left: 0; top: 487px; width: 100%;
    text-align: center; color: var(--paper);
    font-size: 21px; font-weight: 400; line-height: 1; white-space: nowrap;
  }
  .website {
    position: absolute; left: 0; top: 532px; width: 100%;
    text-align: center; color: var(--paper);
    font-size: 18px; font-weight: 400; letter-spacing: 9px; line-height: 1;
  }
</style>
</head>
<body>
  <main class="billboard">
    <header class="masthead">
      <h1 class="brand-name">MAPLE WOVEN</h1>
      <div class="rule rule--top"></div>
    </header>

    <h2 class="headline">WINTER SALES EVENT <span class="dash">-</span> <span class="big">20</span> <span class="light">TO</span> <span class="big">60%</span> <span class="off">OFF</span></h2>

    <div class="product product--bed" role="img" aria-label="Photo of a grey tufted upholstered bed"></div>
    <div class="product product--table" role="img" aria-label="Photo of a round light oak dining table"></div>
    <div class="product product--lamp" role="img" aria-label="Photo of a coral-red sculptural table lamp with black shade"></div>
    <div class="product product--dresser" role="img" aria-label="Photo of a walnut six-drawer dresser with brass pulls"></div>
    <div class="product product--side-table" role="img" aria-label="Photo of a black geometric side table"></div>

    <footer class="footer"></footer>
    <div class="rule rule--bottom"></div>
    <p class="address">3847 22nd Ave SW.CALGARY.AB&nbsp; 403 555 0187</p>
    <p class="website">www.maplewoven.ca</p>
  </main>
</body>
</html>
```